Business Card Design

We would like a business card that utilizes our current logo and keeps with the same feel - elegant and organic. Our farm isn't about mass production, it's about excellence, education, beautiful events and flowers - people, culture, and community.

Target Market(s)

Patrons to our farm who are interested in weddings, events, or our flowers and vegetables.

Contact Information for Business Card

Name, address, cell email (Danielle Hoskins, 2716 Wrenfield Rd, Larkhaven, WL 40127, cell 30.412.6638, email danielle@wrenfieldacres.com)

```html
<!DOCTYPE html>
<html lang="en">
<head>
<meta charset="utf-8">
<title>Wrenfield Acres – Business Card</title>
<link rel="stylesheet" href="https://fonts.googleapis.com/css2?family=Source+Sans+3:wght@400;600;700&display=swap">
<style>
  :root {
    --canvas: #e9e7e3;
    --card: #ffffff;
    --band-top: #a8aaa5;
    --band-bottom: #8e857e;
    --sage: #6f8574;
    --name: #7a6e67;
    --text: #6e6660;
    --rule: #8a837d;
  }
  * { box-sizing: border-box; margin: 0; padding: 0; }
  html, body {
    width: 1200px; height: 900px; overflow: hidden;
    background: var(--canvas);
    font-family: "Source Sans 3", Arial, sans-serif;
  }
  .stage { position: relative; width: 1200px; height: 900px; }
  .card {
    position: absolute; left: 270px;
    width: 660px; height: 376px;
    background: var(--card);
    box-shadow: 0 6px 18px rgba(0,0,0,0.12);
    overflow: hidden;
  }
  .card--front { top: 52px; }
  .card--back { top: 472px; }
  .card__band-top {
    position: absolute; top: 0; left: 0; right: 0; height: 16px;
    background: var(--band-top);
  }
  .card__band-bottom {
    position: absolute; bottom: 0; left: 0; right: 0; height: 24px;
    background: var(--band-bottom);
  }
  .brand {
    position: absolute;
    color: var(--sage);
    font-weight: 400;
    letter-spacing: 0.04em;
    white-space: nowrap;
  }
  .card--front .brand {
    left: 0; right: 0; top: 160px;
    text-align: center; font-size: 40px;
  }
  .card--back .brand {
    left: 0; width: 330px; top: 196px;
    text-align: center; font-size: 30px;
  }
  .divider {
    position: absolute; left: 330px; top: 70px;
    width: 1px; height: 250px; background: var(--rule);
  }
  .contact {
    position: absolute; left: 372px; top: 56px; right: 24px; bottom: 40px;
  }
  .contact__name {
    font-size: 27px; font-weight: 700; color: var(--name);
  }
  .contact__details {
    position: absolute; left: 0; bottom: 0;
    list-style: none;
    font-size: 17px; line-height: 1.45; color: var(--text);
    white-space: nowrap;
  }
</style>
</head>
<body>
<main class="stage">
  <section class="card card--front" aria-label="Business card front">
    <div class="card__band-top"></div>
    <p class="brand">Wrenfield Acres</p>
    <div class="card__band-bottom"></div>
  </section>

  <section class="card card--back" aria-label="Business card back">
    <div class="card__band-top"></div>
    <p class="brand">Wrenfield Acres</p>
    <div class="divider"></div>
    <div class="contact">
      <h1 class="contact__name">Danielle Hoskins</h1>
      <ul class="contact__details">
        <li>30.412.6638</li>
        <li>danielle@wrenfieldacres.com</li>
        <li>Danielle Hoskins, 2716 Wrenfield Rd,</li>
        <li>Larkhaven, WL 40127</li>
      </ul>
    </div>
    <div class="card__band-bottom"></div>
  </section>
</main>
</body>
</html>
```